PELDRAX Business Cards

We require a business card for our company that provides IT consulting services. We already have a logo that needs to be used on the card. We want a clean professional looking design that incorporates our colours. Our main focus is providing managed services to business, which involves us looking after all of their IT requirements including managing servers/networks, projects, and procurement.

Industry/Entity Type

Information Technology

Requirements
Must have
• our logo, contact information, name, title, phone numbers

```html
<!DOCTYPE html>
<html lang="en">
<head>
<meta charset="utf-8">
<title>PELDRAX Business Card</title>
<link href="https://fonts.googleapis.com/css2?family=Jost:wght@400;500;600&family=Lato:wght@300;400&display=swap" rel="stylesheet">
<style>
  :root {
    --brand-blue: #0a8fcc;
    --ink-black: #050505;
    --paper-white: #ffffff;
    --edge-line: #1d1a1a;
    --backdrop: #e8e8e8;
  }
  * { margin: 0; padding: 0; box-sizing: border-box; }
  html, body {
    width: 1200px; height: 872px; overflow: hidden;
    background: var(--backdrop);
  }
  .sheet {
    width: 1200px; height: 872px;
    display: flex; flex-direction: column; align-items: center; justify-content: center;
    gap: 32px;
  }
  .card {
    position: relative; width: 700px; height: 400px; overflow: hidden;
    box-shadow: 0 4px 14px rgba(0,0,0,0.18);
  }
  /* Back side */
  .card--back { background: var(--ink-black); }
  .back-name {
    position: absolute; left: 0; right: 0; top: 140px; text-align: center;
    font-family: "Jost", sans-serif; font-weight: 600; font-size: 84px;
    letter-spacing: 6px; color: var(--brand-blue);
  }
  .back-web {
    position: absolute; left: 0; right: 0; top: 290px; text-align: center;
    font-family: "Lato", sans-serif; font-weight: 400; font-size: 19px;
    letter-spacing: 5px; color: var(--paper-white);
  }
  /* Front side */
  .card--front { background: var(--paper-white); }
  .front-wave { position: absolute; inset: 0; width: 700px; height: 400px; }
  .brand {
    position: absolute; left: 36px; top: 48px;
    display: flex; align-items: center; gap: 14px;
  }
  .brand-dot { width: 40px; height: 40px; border-radius: 50%; background: var(--brand-blue); }
  .brand-name {
    font-family: "Jost", sans-serif; font-weight: 500; font-size: 54px;
    letter-spacing: 5px; color: var(--brand-blue); line-height: 1;
  }
  .contact-list {
    position: absolute; right: 44px; top: 148px; list-style: none;
    font-family: "Lato", sans-serif; font-weight: 400; font-size: 17px;
    color: var(--paper-white); text-align: right;
  }
  .contact-list li {
    display: flex; align-items: center; justify-content: flex-end; gap: 7px;
    height: 25px;
  }
  .contact-list svg, .address svg { width: 13px; height: 13px; fill: none; stroke: var(--paper-white); stroke-width: 1.6; }
  .address {
    position: absolute; right: 44px; top: 296px;
    display: flex; align-items: center; gap: 7px;
    font-family: "Lato", sans-serif; font-size: 16px; color: var(--paper-white);
  }
  .holder { position: absolute; left: 44px; top: 322px; color: var(--paper-white); }
  .holder-name {
    font-family: "Jost", sans-serif; font-weight: 600; font-size: 25px; letter-spacing: 0.5px;
  }
  .holder-title {
    font-family: "Lato", sans-serif; font-weight: 300; font-size: 18px; margin-top: 2px;
  }
</style>
</head>
<body>
<main class="sheet">
  <section class="card card--back" aria-label="Card back">
    <div class="back-name">PELDRAX</div>
    <div class="back-web">www.peldrax.com</div>
  </section>

  <section class="card card--front" aria-label="Card front">
    <svg class="front-wave" viewBox="0 0 700 400" aria-hidden="true">
      <path d="M0 224 C110 230 220 258 300 294 C430 212 570 140 700 98 L700 400 L0 400 Z" fill="var(--brand-blue)"/>
      <path d="M0 214 C110 220 220 248 300 284 C430 202 570 130 700 88" fill="none" stroke="var(--edge-line)" stroke-width="4"/>
    </svg>

    <div class="brand">
      <span class="brand-dot"></span>
      <span class="brand-name">PELDRAX</span>
    </div>

    <ul class="contact-list">
      <li><svg viewBox="0 0 14 14"><path d="M3 1.5 L5.5 4 L4.2 5.6 C5 7.4 6.6 9 8.4 9.8 L10 8.5 L12.5 11 L11 12.5 C6 12.5 1.5 8 1.5 3 Z"/></svg>012-555-0147</li>
      <li><svg viewBox="0 0 14 14"><rect x="3.5" y="1" width="7" height="12" rx="1.2"/><path d="M6 11 H8"/></svg>012-555-0147</li>
      <li><svg viewBox="0 0 14 14"><rect x="1" y="3" width="12" height="8.5"/><path d="M1 3 L7 8 L13 3"/></svg>info@peldrax.com</li>
      <li><svg viewBox="0 0 14 14"><circle cx="7" cy="7" r="5.8"/><ellipse cx="7" cy="7" rx="2.6" ry="5.8"/><path d="M1.2 7 H12.8"/></svg>www.peldrax.com</li>
    </ul>

    <div class="address"><svg viewBox="0 0 14 14"><path d="M7 13 C4 9.5 2.5 7.4 2.5 5.2 A4.5 4.5 0 0 1 11.5 5.2 C11.5 7.4 10 9.5 7 13 Z"/><circle cx="7" cy="5.2" r="1.6"/></svg>Harbor Lane, Westford Zipcode - 04821</div>

    <div class="holder">
      <div class="holder-name">MARCUS HALLBROOK</div>
      <div class="holder-title">PRESIDENT</div>
    </div>
  </section>
</main>
</body>
</html>
```